Tidewell Ventures Wordpress / Web Design - Agile Coaching

UPDATE: PLEASE USE MORE ICONS/GRAPHICS THEN PHOTOS. THANK YOU!

We need a web design for a new company called Tidewell Ventures. We do agile coaching, consulting, training and facilitation for medium to large enterprise, most just starting their agile journey. We want to be professional, but light and whimsical. We have started loading content onto the www.tidewellventures.example website, using the Marlow Theme (real flexibility!)

We have a logo, and I really liked it, although if needed the colors can be adjusted depending on the design. I would advice sticking with the logo and its colors unless they become problematic or you have a fantastic idea.

I really like the colors found on stickum slips, and use stickum slips in all my coaching and training. I want to warn though, I don't want the whole site to be splashes of color, but I would like some pop of color, and you could use the stickum slip colors and the idea of stickum slips for icon designs or sparingly for emphasis, but keep the design simple with lots of white space. I'm inspired by this template from Pattern Bazaar and use the power point in the 2nd attached file...this may inspire you.

I have another contest running right now, if you want to check that out as well, but it isn't necessary. Contest is titled "Tidewell Ventures: Software Development Consultancy Needs a Business Card Design"

Target Market(s)

medium to large software companies needing to improve the speed, quality and value of their software delivery

Industry/Entity Type

Information Technology

Number of Pages Required

3 page

Font styles to use
Sans Serif

Requirements
Must have
• Simple, easy to use, easy navigation, space!
• content on my front page is accurate so should be included www.tidewellventures.example
• 2nd page you can look at is http://www.tidewellventures.example/inspiration/
• 3rd page you can look at is http://www.tidewellventures.example/reference-list/ (about twice as many links are going to be added in next two days!)
Nice to have
• take a look at any other page on the site. if something is password protected, use the word "password" as the password.
• Update: I like less pictures, more graphics.
Should not have
• too crowded. hard to navigate. childish graphics. too boring and corporate. :)

```html
<!DOCTYPE html>
<html lang="en">
<head>
<meta charset="utf-8">
<title>Tidewell Ventures</title>
<link rel="stylesheet" href="https://fonts.googleapis.com/css2?family=Roboto:wght@300;400;500;700&display=swap">
<style>
:root{
  --navy:#0c4d88;
  --navy-dark:#083a68;
  --teal:#18aac6;
  --blue:#1f6fb2;
  --ink:#3a3f45;
  --muted:#6d747b;
  --panel:#ececec;
  --line:#d6d9dc;
  --white:#ffffff;
}
*{box-sizing:border-box;margin:0;padding:0}
html,body{width:778px;height:1200px;overflow:hidden}
body{font-family:"Roboto",sans-serif;color:var(--ink);background:var(--white);position:relative}
a{color:inherit;text-decoration:none}

.site-header{height:64px;display:flex;justify-content:space-between;align-items:center;padding:0 40px}
.brand{display:flex;align-items:center;gap:9px}
.brand-mark{width:26px;height:26px;border-radius:50%;background:var(--teal)}
.brand-name{font-size:19px;font-weight:500;color:var(--navy)}
.header-contact{text-align:right}
.header-tagline{font-size:9px;color:var(--muted)}
.header-phone{display:flex;align-items:center;justify-content:flex-end;gap:5px;font-size:13px;font-weight:700;color:var(--navy);margin-top:3px}

.main-nav{height:24px;background:var(--navy);padding:0 40px;display:flex}
.main-nav a{font-size:9.5px;font-weight:500;color:var(--white);padding:0 11px;line-height:24px;letter-spacing:.3px}
.main-nav a.is-active{background:var(--teal)}

.hero{height:257px;background:linear-gradient(120deg,#cfe3f1 0%,#8fb4cf 35%,#3d6d97 70%,#1e3f63 100%)}

.intro{padding:12px 40px 0;height:120px}
.body-text{font-size:8.5px;line-height:1.55;color:var(--muted)}
.read-more{display:inline-block;font-size:8.5px;color:var(--blue);margin-top:5px}

.welcome{text-align:center;padding:0 40px;height:150px}
.welcome-title{font-size:19px;font-weight:400;color:var(--ink);margin-bottom:10px}
.welcome-title span{color:var(--blue);font-weight:500}

.services{position:relative;height:200px;margin:0 40px;background:var(--panel);padding:14px 58px 0;display:flex;gap:26px}
.service{flex:1;text-align:center}
.service-title{font-size:13px;font-weight:300;color:var(--teal);margin-bottom:8px}
.service-visual{height:62px;border:3px solid var(--white);background:linear-gradient(135deg,#9fc3dd,#4f7fa8)}
.service-text{font-size:8px;line-height:1.5;color:var(--muted);margin-top:8px;text-align:left}
.carousel-arrow{position:absolute;top:84px;width:22px;height:22px}
.carousel-arrow.prev{left:-11px}
.carousel-arrow.next{right:-11px}

.lower{display:flex;gap:24px;padding:22px 40px 0;height:195px}
.lower-col{flex:1}
.lower-title{font-size:14px;font-weight:400;color:var(--ink);border-bottom:1px solid var(--line);padding-bottom:5px;margin-bottom:8px}
.lower-title b{color:var(--blue);font-weight:500}
.update{margin-bottom:10px}
.gallery-visual{height:120px;background:linear-gradient(150deg,#e4e7ea,#9aa3ab 60%,#5b6670)}
.contact-lines{font-size:8px;line-height:1.8;color:var(--muted)}

.site-footer{height:135px;background:var(--navy);padding:14px 40px 0;display:flex;gap:40px}
.footer-col{flex:1}
.footer-title{font-size:10px;color:var(--teal);margin-bottom:6px}
.footer-list{list-style:none;font-size:8px;line-height:1.85;color:var(--white)}
.social li{display:flex;align-items:center;gap:7px}
.social-dot{width:11px;height:11px;background:var(--teal);border-radius:2px}
.follow{flex:0 0 120px}

.footer-bar{height:30px;background:var(--navy-dark);padding:0 40px;display:flex;justify-content:space-between;align-items:center;font-size:7.5px;color:#b9cde0}
.footer-bar nav a{margin-left:8px}
</style>
</head>
<body>

<header class="site-header">
  <div class="brand">
    <span class="brand-mark"></span>
    <span class="brand-name">Tidewell Ventures</span>
  </div>
  <div class="header-contact">
    <p class="header-tagline">Speak to a Communication Specialist 24/7/365</p>
    <p class="header-phone">
      <svg width="11" height="11" viewBox="0 0 24 24"><path fill="#18aac6" d="M6.6 10.8a15.2 15.2 0 0 0 6.6 6.6l2.2-2.2c.3-.3.7-.4 1-.2 1.1.4 2.3.6 3.6.6.6 0 1 .4 1 1V20c0 .6-.4 1-1 1A17 17 0 0 1 3 4c0-.6.4-1 1-1h3.5c.6 0 1 .4 1 1 0 1.3.2 2.5.6 3.6.1.3 0 .7-.2 1z"/></svg>
      1-800-555-0142
    </p>
  </div>
</header>

<nav class="main-nav">
  <a class="is-active" href="#">HOME</a>
  <a href="#">MEMBERSHIP</a>
  <a href="#">COMPANY</a>
  <a href="#">FLEET</a>
  <a href="#">PRESS</a>
  <a href="#">FAQ</a>
  <a href="#">CONTACT</a>
</nav>

<div class="hero" role="img" aria-label="Team members reviewing charts and reports on a tablet at a meeting table"></div>

<section class="intro">
  <p class="body-text">We realize where you are on your agile journey and can help with a little extra infusion of training, or assist in developing a long-term roadmap. Our coaches work beside your teams to shape steady habits, clear goals and a calm delivery rhythm that grows value with every release and lasting trust.</p>
  <a class="read-more" href="#">Read More...</a>
</section>

<section class="welcome">
  <h1 class="welcome-title">Welcome to <span>Tidewell Ventures</span></h1>
  <p class="body-text">Agile change works best when people feel supported. We guide leaders and teams through planning, coaching and hands-on practice so that new ways of working take root. Each engagement is shaped around your goals, your culture and your pace, with simple tools and honest feedback at every step of the way forward.</p>
  <a class="read-more" href="#">Read More...</a>
</section>

<section class="services">
  <svg class="carousel-arrow prev" viewBox="0 0 22 22"><circle cx="11" cy="11" r="11" fill="#18aac6"/><path d="M13 6l-5 5 5 5" stroke="#fff" stroke-width="2.4" fill="none"/></svg>
  <article class="service">
    <h2 class="service-title">Consulting</h2>
    <div class="service-visual" role="img" aria-label="Hand pointing at a business chart"></div>
    <p class="service-text">Lorem ipsum dolor sit amet, consectetur adipiscing elit, sed do eiusmod tempor incididunt ut labore et dolore magna aliqua.</p>
  </article>
  <article class="service">
    <h2 class="service-title">Training</h2>
    <div class="service-visual" role="img" aria-label="Training session in a meeting room"></div>
    <p class="service-text">Lorem ipsum dolor sit amet, consectetur adipiscing elit, sed do eiusmod tempor incididunt ut labore et dolore magna aliqua.</p>
  </article>
  <article class="service">
    <h2 class="service-title">Coaching</h2>
    <div class="service-visual" role="img" aria-label="Coach working one-on-one with a colleague"></div>
    <p class="service-text">Lorem ipsum dolor sit amet, consectetur adipiscing elit, sed do eiusmod tempor incididunt ut labore et dolore magna aliqua.</p>
  </article>
  <svg class="carousel-arrow next" viewBox="0 0 22 22"><circle cx="11" cy="11" r="11" fill="#18aac6"/><path d="M9 6l5 5-5 5" stroke="#fff" stroke-width="2.4" fill="none"/></svg>
</section>

<section class="lower">
  <div class="lower-col">
    <h2 class="lower-title"><b>Our</b> Latest Updates</h2>
    <div class="update">
      <p class="body-text">Lorem ipsum dolor sit amet, consectetur adipiscing elit, sed do eiusmod tempor incididunt ut labore.</p>
      <a class="read-more" href="#">Read More...</a>
    </div>
    <div class="update">
      <p class="body-text">Lorem ipsum dolor sit amet, consectetur adipiscing elit, sed do eiusmod tempor incididunt ut labore.</p>
      <a class="read-more" href="#">Read More...</a>
    </div>
  </div>
  <div class="lower-col">
    <h2 class="lower-title"><b>Our</b> Gallery</h2>
    <div class="gallery-visual" role="img" aria-label="Gallery photo of a workshop with a laptop and notes"></div>
  </div>
  <div class="lower-col">
    <h2 class="lower-title"><b>Contact</b> Address</h2>
    <p class="contact-lines">Your Mailing Address<br>4120 Harbor Point Lane<br>Marlow Bay, OR 97000<br><br>Phone: (503) 555-0186<br><br>Email: hello@tidewellventures.example</p>
  </div>
</section>

<footer class="site-footer">
  <div class="footer-col">
    <h3 class="footer-title">Company</h3>
    <ul class="footer-list">
      <li>Home</li><li>About Us</li><li>Careers</li><li>Events</li><li>Press Room</li>
    </ul>
  </div>
  <div class="footer-col">
    <h3 class="footer-title">Our Company Services</h3>
    <ul class="footer-list">
      <li>Service Text Title Here</li><li>Service Text Title Here</li><li>Service Text Title Here</li><li>Service Text Title Here</li><li>Service Text Title Here</li>
    </ul>
  </div>
  <div class="footer-col follow">
    <h3 class="footer-title">Follow us on</h3>
    <ul class="footer-list social">
      <li><span class="social-dot"></span>Chirpline</li>
      <li><span class="social-dot"></span>Linkfold</li>
      <li><span class="social-dot"></span>Friendboard</li>
      <li><span class="social-dot"></span>Circlespace</li>
    </ul>
  </div>
</footer>

<div class="footer-bar">
  <p>Copyright © 2015 Tidewell Ventures. All rights reserved.</p>
  <nav><a href="#">Terms of Use</a> | <a href="#">Privacy Policy</a> | <a href="#">Contact Us</a></nav>
</div>

</body>
</html>
```